Wine label design for a family winery in Slovenia

We need new label design for our wines.
We are small family wine producers who focuses on good quality wine and loves to experiment, mixing tradition with new, more modern approaches. Our main product is ‘Teran’, red wine whose character is highly defined by terroir: more acidic, but rich body and very rich, dark colour (we say it's not red, but black). We also age a small portion of this Teran wine with wood, which we named 'Kamnje' (after one of our vineyards). From the same grapes as Teran we also produce a small quantity of Rose. And we also produce two white wine varieties: one is 'Zorn', cuvee of several different sorts of grapes. The other is 'Pečine', Chardonnay wine, named after another of our vineyards. Aside from all that we also produce liquour (Teranov liker) made from Teran wine and a small quantity of other spirits (Grappa, various fruit liquors, a version of Hügelbrand, and ‘Travarica’ which is grappa infused with various herbs and spices).
Zorn, Rose and Teran are considered our 'basic' line, whereas 'Kamnje' and 'Pečine' are considered to be a higher quality line. Rose sits somewhere between this two.
In time we'd like to renew all of our labels. But the priority and subject of this ‘’project’’ is to create the two for our top line, Kamnje and Pečine and also for Rose.
For 'Kamnje' we already have a template label. The general idea behind it was play with letters and divide them along the label (KA MN JE). We found that we like the narrow, longer dimensions and that black label on black bottle, with letters that stand out due to colour or printing differences, work very well. But we're amateurs and the label is not finalized. We would ask you to do something on this basis, but please don't limit yourself only to this if you have a better idea.
For 'Pečine' the label should be in the same style to imply the same higher quality line - colours can and probably should be reversed to the lighter side (so to imply that it’s a white wine). Also, for this wine we'll use the same dark slender bottles, like you see on the image.
Please keep in mind that we'll print smaller series (1000-2000 pcs), so it must be possible to print the labels for a sensible cost. Solutions like classical offset gold print that requires large series of 10.000 pcs, will not work. But we can look into any digital printing/lacquering options that offer similar effects. Anyway, we are not experts on this field, so your advice on printing techniques is also welcomed.
Also, a word on our emblem: the logo is also not finalized and we will also ask you to work on it. The logo is part of the ornament on the doors of our homestead and represents a ‘kolovrat’ (‘spinning wheel’ in English), an old Slavic symbol for the sun, representing eternal life and spinning of time. We'd like to use it, but right now it's badly digitalized. If you'll need any better photos of it, let me know.

Target Market(s)

30-60 yo, red wine lovers, appreciate local and speicality wines

Font styles to use
Sans Serif
Decorative

Requirements
Must have
• long, narrow label dimensions (see attached Kamnje)

```html
<!DOCTYPE html>
<html lang="sl">
<head>
<meta charset="utf-8">
<title>Kraška klet Lipar – Kamnje &amp; Pečine</title>
<link rel="stylesheet" href="https://fonts.googleapis.com/css2?family=Playfair+Display:wght@400&family=Roboto:wght@300;400&display=swap">
<style>
:root{
  --bg:#ededed;
  --black:#060606;
  --white:#ffffff;
  --red:#d4232b;
  --gold:#b8914f;
  --dim-dark:#2a2a2a;
  --dim-light:#c9c9c9;
  --grey-on-dark:#8a8a8a;
  --grey-on-light:#444444;
  --serif:"Playfair Display", serif;
  --sans:"Roboto", sans-serif;
}
*{margin:0;padding:0;box-sizing:border-box}
html,body{width:1200px;height:1027px;overflow:hidden;background:var(--bg)}
.canvas{position:relative;width:1200px;height:1027px;background:var(--bg);font-family:var(--sans)}

.label{position:absolute;overflow:hidden;text-align:center}
.label--front{width:190px;height:453px;top:417px}
.label--back{width:192px;height:257px;top:505px}
.label--dark{background:var(--black);color:var(--grey-on-dark)}
.label--light{background:var(--white);color:var(--grey-on-light)}

.kamnje-front{left:112px}
.kamnje-back{left:365px}
.pecine-front{left:671px}
.pecine-back{left:937px}

/* brand block */
.brand{position:absolute;left:0;right:0;top:30px;display:flex;flex-direction:column;align-items:center}
.brand__dot{width:26px;height:26px;border-radius:50%;margin-bottom:10px}
.brand__line1{font-size:9px;letter-spacing:1px;font-weight:400}
.brand__line2{font-size:14px;letter-spacing:6px;font-weight:400;margin-top:1px}
.label--dark .brand{color:var(--white)}
.label--light .brand{color:#111}
.label--dark .brand__dot{background:var(--red)}
.label--light .brand__dot{background:var(--gold)}

.brand--row{top:10px;flex-direction:row;justify-content:center;gap:6px}
.brand--row .brand__dot{width:22px;height:22px;margin:0}
.brand--row .brand__text{text-align:left}
.brand--row .brand__line1{font-size:8px}
.brand--row .brand__line2{font-size:12px;letter-spacing:5px;margin-top:0}

/* letter play */
.play{position:absolute;white-space:nowrap;font-family:var(--serif);font-size:60px;line-height:1}
.play span.hi{color:var(--accent)}
.label--dark .play{color:var(--dim-dark);--accent:var(--red)}
.label--light .play{color:var(--dim-light);--accent:var(--gold)}
.play--1{top:148px;left:8px}
.play--2{top:200px;left:-19px}
.play--3{top:254px;left:-51px}

.vintage{position:absolute;left:0;right:0;top:400px;font-size:13px;font-weight:300}
.made{position:absolute;left:0;right:0;top:434px;font-size:8.5px;letter-spacing:.3px;font-weight:300}
.label--light .vintage,.label--light .made{color:#333}

/* back label */
.back__region{position:absolute;left:0;right:0;top:56px;font-size:8.5px;font-weight:300;letter-spacing:.3px}
.back__name{position:absolute;left:0;right:0;top:70px;font-family:var(--serif);font-weight:400;font-size:34px;line-height:1}
.label--dark .back__name{color:var(--red)}
.label--light .back__name{color:var(--gold)}
.back__variety{position:absolute;left:0;right:0;top:110px;font-size:12px;letter-spacing:1px;font-weight:300}
.label--light .back__variety{color:#111;font-weight:400}
.back__meta{position:absolute;left:0;right:0;top:124px;font-size:7.5px;line-height:9.5px;font-weight:300}
.back__text{position:absolute;left:10px;right:10px;top:154px;font-size:7.5px;line-height:9.5px;font-weight:300}
.back__legal{position:absolute;left:6px;right:6px;top:196px;font-size:7.5px;line-height:9.5px;font-weight:300}
.back__foot{position:absolute;left:13px;right:13px;top:240px;display:flex;justify-content:space-between;font-size:9px}
.label--dark .back__foot{color:var(--red)}
.label--light .back__foot{color:var(--gold)}
</style>
</head>
<body>
<main class="canvas">

  <section class="label label--front label--dark kamnje-front">
    <div class="brand">
      <span class="brand__dot"></span>
      <span class="brand__line1">KRAŠKA KLET</span>
      <span class="brand__line2">LIPAR</span>
    </div>
    <div class="play play--1"><span class="hi">KA</span>MNJE</div>
    <div class="play play--2">KA<span class="hi">MN</span>JEKA</div>
    <div class="play play--3">KAMN<span class="hi">JE</span>K</div>
    <p class="vintage">2017</p>
    <p class="made">IZDELANO V SLOVENIJI</p>
  </section>

  <section class="label label--back label--dark kamnje-back">
    <div class="brand brand--row">
      <span class="brand__dot"></span>
      <div class="brand__text">
        <div class="brand__line1">KRAŠKA KLET</div>
        <div class="brand__line2">LIPAR</div>
      </div>
    </div>
    <p class="back__region">VINORODNI OKOLIŠ KRAS</p>
    <h2 class="back__name">KAMNJE</h2>
    <p class="back__variety">TERAN PTP</p>
    <p class="back__meta">suho vino<br>2017</p>
    <p class="back__text">Izdelan po tradicionalnem postopku iz izbranega grozdja teranovk s Liparjevih starih brajd na Kamnju.</p>
    <p class="back__legal">Vsebuje sulfit.<br>Št. polnitve: 07-2018. Št. odločbe: KP-217/2018.<br>IZDELANO V SLOVENIJI - MADE IN SLOVENIA</p>
    <div class="back__foot"><span>11,0 % vol</span><span>0,75 l</span></div>
  </section>

  <section class="label label--front label--light pecine-front">
    <div class="brand">
      <span class="brand__dot"></span>
      <span class="brand__line1">KRAŠKA KLET</span>
      <span class="brand__line2">LIPAR</span>
    </div>
    <div class="play play--1"><span class="hi">PE</span>ČINE</div>
    <div class="play play--2">PE<span class="hi">ČI</span>NEPE</div>
    <div class="play play--3">PEČI<span class="hi">NE</span>P</div>
    <p class="vintage">2017</p>
    <p class="made">IZDELANO V SLOVENIJI</p>
  </section>

  <section class="label label--back label--light pecine-back">
    <div class="brand brand--row">
      <span class="brand__dot"></span>
      <div class="brand__text">
        <div class="brand__line1">KRAŠKA KLET</div>
        <div class="brand__line2">LIPAR</div>
      </div>
    </div>
    <p class="back__region">VINORODNI OKOLIŠ KRAS</p>
    <h2 class="back__name">PEČINE</h2>
    <p class="back__variety">CHARDONNAY</p>
    <p class="back__meta">suho vino<br>2017</p>
    <p class="back__text">Izdelan po tradicionalnem postopku iz izbranega grozdja teranovk s Liparjevih starih brajd na Kamnju.</p>
    <p class="back__legal">Vsebuje sulfit.<br>Št. polnitve: 07-2018. Št. odločbe: KP-217/2018.<br>IZDELANO V SLOVENIJI - MADE IN SLOVENIA</p>
    <div class="back__foot"><span>11,0 % vol</span><span>0,75 l</span></div>
  </section>

</main>
</body>
</html>
```